Podcast Cover Art for Fast Growing Show (Ill include a gracious tip!)

This artwork is for "The Steadfast Fellow Show." The podcast is for men, and it's all about self-improvement, confidence, success, money, women and masculinity. It's for the guy who wants to improve himself. I'd like for my picture to be included — in black and white — and I want the text to read: "The Steadfast Fellow Show" and somewhere in there it'll say: "with Dale Prowen." I'm open to color schemes. The podcast is a little edgy so I'd like for that to be represented in the design. Thank you! (((Here's the podcast page if you wanna check it out: http://steadfastfellowshow.castorbit.net/)))

Target Market(s)

Men who want to attract women and improve their lives!

Font styles to use
Serif

Colors

Designer to choose colors to be used in the design.

Requirements
Must have
• My image in it (in black and white) and the two titles: "The Steadfast Fellow Show" and "with Dale Prowen"
Nice to have
• My logo in it somehow (which is the arrow looking logo attached below). I've also found that my image looks best in black and white and with a circular type cut out (although I'm open to different design ideas). I've attached my logo with a circular cut out below so you can see what I'm talking about.
Should not have
• Flowers. Teddy bears. ice cream.

```html
<!DOCTYPE html>
<html lang="en">
<head>
<meta charset="utf-8">
<title>The Steadfast Fellow Show — Cover Art</title>
<link rel="stylesheet" href="https://fonts.googleapis.com/css2?family=Advent+Pro:wght@300;400&display=swap">
<style>
  :root {
    --bg: #0c0c0c;
    --band-dark: #1b1b1b;
    --band-mid: #262626;
    --band-light: #353535;
    --band-pale: #414141;
    --portrait-light: #5a5a5a;
    --portrait-dark: #3a3a3a;
    --text: #ffffff;
  }
  html, body {
    margin: 0;
    padding: 0;
    width: 1200px;
    height: 1200px;
    overflow: hidden;
    background: var(--bg);
  }
  .cover {
    display: block;
    width: 1200px;
    height: 1200px;
  }
  .cover__title,
  .cover__host {
    font-family: "Advent Pro", "Arial Narrow", sans-serif;
    font-weight: 300;
    fill: var(--text);
  }
  .band--dark { stroke: var(--band-dark); }
  .band--mid { stroke: var(--band-mid); }
  .band--light { stroke: var(--band-light); }
  .band--pale { stroke: var(--band-pale); }
  .band { fill: none; stroke-width: 120; stroke-linejoin: miter; }
</style>
</head>
<body>
<svg class="cover" viewBox="0 0 1200 1200" xmlns="http://www.w3.org/2000/svg">
  <defs>
    <radialGradient id="portraitTone" cx="50%" cy="40%" r="60%">
      <stop offset="0%" stop-color="var(--portrait-light)"/>
      <stop offset="100%" stop-color="var(--portrait-dark)"/>
    </radialGradient>
    <linearGradient id="lowerShade" x1="0" y1="0" x2="0" y2="1">
      <stop offset="0%" stop-color="#000" stop-opacity="0.35"/>
      <stop offset="60%" stop-color="#000" stop-opacity="0"/>
    </linearGradient>
    <filter id="softShadow" x="-10%" y="-10%" width="120%" height="130%">
      <feDropShadow dx="3" dy="4" stdDeviation="3" flood-color="#000" flood-opacity="0.7"/>
    </filter>
  </defs>

  <rect class="cover__backdrop" width="1200" height="1200" fill="var(--bg)"/>

  <g class="cover__chevrons">
    <polyline class="band band--dark"  points="-300,-650 600,250 1500,-650"/>
    <polyline class="band band--mid"   points="-300,-490 600,410 1500,-490"/>
    <polyline class="band band--dark"  points="-300,-330 600,570 1500,-330"/>
    <polyline class="band band--light" points="-300,-170 600,730 1500,-170"/>
    <polyline class="band band--mid"   points="-300,-10 600,890 1500,-10"/>
    <polyline class="band band--pale"  points="-300,150 600,1050 1500,150"/>
    <polyline class="band band--light" points="-300,310 600,1210 1500,310"/>
    <polyline class="band band--mid"   points="-300,470 600,1370 1500,470"/>
    <polyline class="band band--dark"  points="-300,630 600,1530 1500,630"/>
    <polyline class="band band--light" points="-300,790 600,1690 1500,790"/>
    <rect width="1200" height="1200" fill="url(#lowerShade)"/>
  </g>

  <circle class="cover__portrait" cx="593" cy="709" r="309"
          fill="url(#portraitTone)" role="img"
          aria-label="Black and white portrait of host Dale Prowen, hands steepled in front of his chin"/>

  <g class="cover__title" filter="url(#softShadow)">
    <text x="600" y="240" text-anchor="middle">
      <tspan font-size="190">The</tspan><tspan font-size="250" dx="10">Steadfast</tspan>
    </text>
    <text x="600" y="425" text-anchor="middle">
      <tspan font-size="200">Fellow</tspan><tspan font-size="110" dx="22">Show</tspan>
    </text>
  </g>

  <g class="cover__host" filter="url(#softShadow)">
    <text x="600" y="1112" text-anchor="middle">
      <tspan font-size="130">with</tspan><tspan font-size="205" dx="14">Dale Prowen</tspan>
    </text>
  </g>
</svg>
</body>
</html>
```